New design for 4 homepage screens (no full design) --> Follow-up business for winner

- Please make sure to read these instructions and the PowerPoint File attached
- Varnoki.com is a Swiss-based online store selling business shirts and accessories for business men
- Please visit the page to make yourself familiar with the company. Although the text is in German, with Google translator you should be able to understand the main content.
- Our clients are mainly business men between 30 and 60 years old. Mostly with a high income working in the service industry (banking, insurance, lawyers, etc.). Sometimes there wives purchase the shirts for them ;-)
- The store is based on Crateloom, so you cannot change the layout freely
- The colors and the logo are given, as they are also used for the print materials (please see files in attachment)
- I am running several business and often need a talented web designer --> the winner gets substantial follow-up business

- Your tasks:
- Please design the four screens you can use in the carousel on the homepage
- The design we use today did not receive good enough feedback
- You are free to use graphic elements or (stock) photos (real or Photoshoped). If you are using photos, they must be properly licensed. If license cost are above US$ 100 please check with me in advance.
- Please make sure the text is not too boring, it is OK, if it is a bit hard to read, not all words same size, different alignment or something like this.
- In the attached file, you can find the text that needs to be on the screens. You do not need to use bullet points or stick to the colors, they are just for illustration purposes.
- The Englisch translation on the right-hand side, is just for you – please use the German texts in you design proposals
- At the end of the day, the conversion is key – so first you need to make sure visitors don’t just jump off the page after their first impression and that they browse to the shop. You can use links to connect with other pages (see current version)

Target Market(s)

Men's business shirts and accessoiries

Industry/Entity Type

Business

Number of Pages Required

4 page

Font styles to use
Other font styles liked:
• Presto

Requirements
Must have
• - Match to the existing logo and colors
• - Fit with target audience (business men 30-60 years old)
Nice to have
• Fits with the key terms of our brand:
• - Successful in your job
• - Performance oriented
• - Fast, simple, easy

```html
<!DOCTYPE html>
<html lang="de">
<head>
<meta charset="utf-8">
<title>Varnoki – Business Hemden und Accessoires</title>
<link href="https://fonts.googleapis.com/css2?family=Open+Sans:wght@400;600;700&family=Playfair+Display:wght@400;700&display=swap" rel="stylesheet">
<style>
:root{
  --black:#111111;
  --ink:#2a2a2a;
  --muted:#6b6b6b;
  --gold:#c9a24b;
  --gold-dark:#a9843a;
  --hero:#1d242b;
  --hero-light:#3a4651;
  --card-bg:#ffffff;
  --tile:#f2f2f2;
  --price:#e6e6e6;
  --line:#dcdcdc;
  --footer:#1b1b1b;
  --footer-deep:#0f0f0f;
}
*{box-sizing:border-box;margin:0;padding:0}
html,body{width:1200px;height:2748px;overflow:hidden}
body{position:relative;background:#fff;font-family:"Open Sans",Arial,sans-serif;color:var(--ink)}

.topbar{position:absolute;top:0;left:0;width:1200px;height:32px;background:var(--black);color:#cfcfcf;font-size:11px;display:flex;align-items:center;justify-content:space-between;padding:0 160px}
.topbar .promo{color:var(--gold)}

.masthead{position:absolute;top:32px;left:0;width:1200px;height:116px;display:flex;align-items:center;justify-content:center}
.brand{display:flex;flex-direction:column;align-items:center;gap:8px}
.brand .mark{width:34px;height:34px;background:var(--gold)}
.brand .name{font-family:"Open Sans",Arial,sans-serif;font-weight:600;font-size:34px;letter-spacing:6px;color:var(--gold)}

.mainnav{position:absolute;top:148px;left:0;width:1200px;height:36px;background:var(--black)}
.mainnav ul{list-style:none;display:flex;gap:38px;padding-left:176px;height:100%;align-items:center}
.mainnav li{color:#fff;font-size:11px;font-weight:600;letter-spacing:1px}

.hero{position:absolute;top:184px;left:0;width:1200px;height:476px;background:linear-gradient(90deg,var(--hero-light) 0%,var(--hero) 45%,#141a20 100%)}
.hero .portrait{position:absolute;left:170px;top:0;width:340px;height:476px;background:linear-gradient(180deg,#2c2f33 0%,#15181b 100%)}
.hero .copy{position:absolute;left:600px;top:70px;color:#fff}
.hero h1{font-family:"Playfair Display",Georgia,serif;font-weight:400;font-size:52px;margin-bottom:30px}
.hero p{font-size:17px;line-height:1.4;margin-bottom:30px;max-width:460px}
.hero .arrow{position:absolute;top:190px;width:36px;height:96px;background:rgba(210,210,210,.85);display:flex;align-items:center;justify-content:center}
.hero .arrow.prev{left:0}
.hero .arrow.next{right:0}

.category{position:absolute;left:0;width:1200px}
.category-title{display:flex;align-items:center;gap:22px;width:880px;margin:0 auto;font-size:19px;font-weight:600;letter-spacing:2px;color:var(--ink)}
.category-title::before,.category-title::after{content:"";flex:1;height:2px;background:var(--gold)}
.carousel{position:relative;width:880px;margin:34px auto 0;display:flex;gap:26px}
.carousel .nudge{position:absolute;top:140px;font-size:22px;color:#9a9a9a}
.carousel .nudge.prev{left:-30px}
.carousel .nudge.next{right:-30px}

.product{width:200px;background:var(--card-bg);border:1px solid var(--line);box-shadow:0 1px 4px rgba(0,0,0,.08)}
.product .photo{height:190px;margin:8px;display:block}
.product .badge{height:26px;background:var(--black);color:#fff;font-size:10px;font-weight:600;display:flex;align-items:center;justify-content:center}
.product .badge.deal{background:var(--gold);color:#fff}
.product .desc{padding:10px 10px 6px;text-align:center;font-size:10px;line-height:1.45;color:var(--muted);height:58px}
.product .price{margin:0 10px 10px;background:var(--price);font-size:10px;font-weight:700;text-align:center;padding:5px 0;color:var(--ink)}

.footer{position:absolute;top:2470px;left:0;width:1200px;height:278px;background:var(--footer);color:#bdbdbd}
.footer .cols{position:absolute;top:30px;left:160px;width:880px;display:flex;justify-content:space-between}
.footer h4{color:var(--gold);font-size:13px;letter-spacing:1px;margin-bottom:14px}
.footer li{list-style:none;font-size:11px;line-height:22px}
.footer li::before{content:"› ";color:var(--gold)}
.footer .col{width:250px}
.footer .news p{font-size:11px;line-height:1.5;margin-bottom:12px}
.footer .signup{display:flex}
.footer .signup span{flex:1;height:28px;background:#2b2b2b;border:1px solid #3a3a3a;font-size:10px;padding:6px 8px;color:#777}
.footer .signup b{width:36px;height:28px;background:#444;font-size:10px;display:flex;align-items:center;justify-content:center;color:#eee}
.footer .contact div{display:flex;align-items:center;gap:10px;font-size:11px;line-height:24px}
.footer .follow{position:absolute;top:170px;left:160px}
.footer .follow .dots{display:flex;gap:8px}
.footer .follow .dots i{width:22px;height:22px;border-radius:50%;background:#3a3a3a;display:block}
.footer .legal{position:absolute;bottom:0;left:0;width:1200px;height:40px;background:var(--footer-deep);display:flex;align-items:center;justify-content:space-between;padding:0 160px;font-size:10px;color:#888}
.footer .legal .up{width:22px;height:22px;border:1px solid #555;border-radius:50%;display:flex;align-items:center;justify-content:center}
</style>
</head>
<body>

<div class="topbar">
  <span>Mein Konto ▾ &nbsp; Hilfe</span>
  <span class="promo">Versandkostenfrei ab CHF 100 – 3 Tage Lieferung</span>
  <span>Anmelden &nbsp; | &nbsp; Warenkorb (0)</span>
</div>

<header class="masthead">
  <div class="brand"><span class="mark"></span><span class="name">VARNOKI</span></div>
</header>

<nav class="mainnav">
  <ul>
    <li>HOME</li><li>ONLINE SHOP ▾</li><li>ANGEBOT ▾</li><li>VARNOKI ▾</li><li>NEWS</li><li>KONTAKT</li>
  </ul>
</nav>

<section class="hero">
  <div class="portrait" role="img" aria-label="Mann im dunklen Anzug mit Fliege und weissem Hemd"></div>
  <div class="copy">
    <h1>Passend:</h1>
    <p>Der ultimative Business Look für erfolgreiche Tage im Büro</p>
    <p>114 Grössen: 4 Breiten, 3 Längen, viele Kragenweiten</p>
    <p>Alle Modelle in allen Grössen verfügbar</p>
  </div>
  <div class="arrow prev"><svg width="14" height="26" viewBox="0 0 14 26"><path d="M12 2 2 13l10 11" fill="none" stroke="#555" stroke-width="2"/></svg></div>
  <div class="arrow next"><svg width="14" height="26" viewBox="0 0 14 26"><path d="M2 2l10 11L2 24" fill="none" stroke="#555" stroke-width="2"/></svg></div>
</section>

<section class="category" style="top:702px">
  <h2 class="category-title">HEMDEN</h2>
  <div class="carousel">
    <span class="nudge prev">‹</span><span class="nudge next">›</span>
    <article class="product"><span class="photo" role="img" aria-label="Weisses Businesshemd gefaltet" style="background:linear-gradient(#f7f7f9,#e4e6ea)"></span><div class="badge deal">Varnoki – Aktuell! Tiefpreis</div><p class="desc">Lila Businesshemd feines Streifenmuster Slim Fit</p><div class="price">CHF 59.00 statt CHF 89.00</div></article>
    <article class="product"><span class="photo" role="img" aria-label="Hellblaues Businesshemd gefaltet" style="background:linear-gradient(#eef3f9,#d6e1ee)"></span><div class="badge deal">Varnoki – Aktuell! Tiefpreis</div><p class="desc">Hellblaues Hemd mit feinem Karo Slim Fit</p><div class="price">CHF 59.00 statt CHF 89.00</div></article>
    <article class="product"><span class="photo" role="img" aria-label="Blaues Businesshemd gefaltet" style="background:linear-gradient(#dfe8f4,#b9cbe3)"></span><div class="badge deal">Varnoki – Aktuell! Tiefpreis</div><p class="desc">Blaues Hemd mit Haifischkragen Regular Fit</p><div class="price">CHF 59.00 statt CHF 89.00</div></article>
    <article class="product"><span class="photo" role="img" aria-label="Weisses Hemd gefaltet" style="background:linear-gradient(#fafafa,#e8e8e8)"></span><div class="badge deal">Varnoki – Aktuell! Tiefpreis</div><p class="desc">Weisses Hemd Twill Struktur Slim Fit</p><div class="price">CHF 59.00 statt CHF 89.00</div></article>
  </div>
</section>

<section class="category" style="top:1150px">
  <h2 class="category-title">KRAWATTEN &amp; EINSTECKTÜCHER</h2>
  <div class="carousel">
    <span class="nudge prev">‹</span><span class="nudge next">›</span>
    <article class="product"><span class="photo" role="img" aria-label="Dunkelrote Krawatte" style="background:linear-gradient(90deg,#f4f4f4 40%,#5e1a24 40%,#5e1a24 60%,#f4f4f4 60%)"></span><div class="badge">Preisname</div><p class="desc">Bordeauxrote Seidenkrawatte uni</p><div class="price">CHF 39.00</div></article>
    <article class="product"><span class="photo" role="img" aria-label="Rote Krawatte" style="background:linear-gradient(90deg,#f4f4f4 40%,#8a1f2a 40%,#8a1f2a 60%,#f4f4f4 60%)"></span><div class="badge">Preisname</div><p class="desc">Rote Seidenkrawatte feine Struktur</p><div class="price">CHF 39.00</div></article>
    <article class="product"><span class="photo" role="img" aria-label="Gemustertes braunes Einstecktuch" style="background:radial-gradient(circle,#5a2a22 55%,#f4f4f4 56%)"></span><div class="badge">Preisname</div><p class="desc">Einstecktuch aus Seide braun</p><div class="price">CHF 29.00</div></article>
    <article class="product"><span class="photo" role="img" aria-label="Blaue Krawatte" style="background:linear-gradient(90deg,#f4f4f4 40%,#1f3fb8 40%,#1f3fb8 60%,#f4f4f4 60%)"></span><div class="badge">Preisname</div><p class="desc">Königsblaue Seidenkrawatte uni</p><div class="price">CHF 39.00</div></article>
  </div>
</section>

<section class="category" style="top:1590px">
  <h2 class="category-title">MANSCHETTENKNÖPFE</h2>
  <div class="carousel">
    <span class="nudge prev">‹</span><span class="nudge next">›</span>
    <article class="product"><span class="photo" role="img" aria-label="Silberne Manschettenknöpfe" style="background:radial-gradient(ellipse at center,#c9cdd2 20%,#f4f4f4 45%)"></span><div class="badge">Preisname</div><p class="desc">Manschettenknöpfe Silber mit Gravur</p><div class="price">CHF 49.00</div></article>
    <article class="product"><span class="photo" role="img" aria-label="Manschettenknöpfe mit roter Fläche" style="background:radial-gradient(ellipse at center,#8f1e3a 20%,#f4f4f4 45%)"></span><div class="badge">Preisname</div><p class="desc">Manschettenknöpfe Silber Emaille rot</p><div class="price">CHF 49.00</div></article>
    <article class="product"><span class="photo" role="img" aria-label="Weisse Manschettenknöpfe" style="background:radial-gradient(ellipse at center,#e2e2e2 20%,#f7f7f7 45%)"></span><div class="badge">Preisname</div><p class="desc">Manschettenknöpfe Perlmutt quadratisch</p><div class="price">CHF 49.00</div></article>
    <article class="product"><span class="photo" role="img" aria-label="Manschettenknöpfe in Bordeaux" style="background:radial-gradient(ellipse at center,#6b2a3a 20%,#f4f4f4 45%)"></span><div class="badge">Preisname</div><p class="desc">Manschettenknöpfe Silber Stein dunkelrot</p><div class="price">CHF 49.00</div></article>
  </div>
</section>

<section class="category" style="top:2030px">
  <h2 class="category-title">GÜRTEL</h2>
  <div class="carousel">
    <span class="nudge prev">‹</span><span class="nudge next">›</span>
    <article class="product"><span class="photo" role="img" aria-label="Brauner Ledergürtel" style="background:radial-gradient(ellipse at center,#7a4a2a 32%,#f4f4f4 50%)"></span><div class="badge">Preisname</div><p class="desc">Ledergürtel braun Dornschliesse</p><div class="price">CHF 69.00</div></article>
    <article class="product"><span class="photo" role="img" aria-label="Dunkelbrauner Ledergürtel" style="background:radial-gradient(ellipse at center,#4a2c1c 32%,#f4f4f4 50%)"></span><div class="badge">Preisname</div><p class="desc">Ledergürtel dunkelbraun glatt</p><div class="price">CHF 69.00</div></article>
    <article class="product"><span class="photo" role="img" aria-label="Schwarzer Ledergürtel" style="background:radial-gradient(ellipse at center,#1c1c1c 32%,#f4f4f4 50%)"></span><div class="badge">Preisname</div><p class="desc">Ledergürtel schwarz Silberschliesse</p><div class="price">CHF 69.00</div></article>
    <article class="product"><span class="photo" role="img" aria-label="Schwarzer Ledergürtel mit Struktur" style="background:radial-gradient(ellipse at center,#262626 32%,#f4f4f4 50%)"></span><div class="badge">Preisname</div><p class="desc">Ledergürtel schwarz geprägt</p><div class="price">CHF 69.00</div></article>
  </div>
</section>

<footer class="footer">
  <div class="cols">
    <div class="col">
      <h4>NAVIGATION</h4>
      <ul><li>Online Shop</li><li>Über uns</li><li>AGB</li></ul>
    </div>
    <div class="col news">
      <h4>In Verbindung Bleiben</h4>
      <p>Abonnieren Sie unseren Newsletter und erhalten Sie Angebote zuerst.</p>
      <div class="signup"><span>E-Mail Adresse</span><b>OK</b></div>
    </div>
    <div class="col contact">
      <h4>Kontaktiere Uns</h4>
      <div><svg width="12" height="14" viewBox="0 0 12 14"><path d="M6 13S1 8 1 5a5 5 0 0 1 10 0c0 3-5 8-5 8z" fill="var(--gold)"/></svg>Varnoki GmbH, Musterweg 12, 8000 Zürich</div>
      <div><svg width="12" height="12" viewBox="0 0 12 12"><path d="M2 1h3l1 3-2 1a7 7 0 0 0 3 3l1-2 3 1v3c-6 0-9-3-9-9z" fill="var(--gold)"/></svg>+41 00 000 00 00</div>
      <div><svg width="12" height="10" viewBox="0 0 12 10"><rect x="0.5" y="0.5" width="11" height="9" fill="none" stroke="var(--gold)"/><path d="M1 1l5 4 5-4" fill="none" stroke="var(--gold)"/></svg>info@varnoki.com</div>
    </div>
  </div>
  <div class="follow">
    <h4>Folge uns</h4>
    <div class="dots"><i></i><i></i><i></i></div>
  </div>
  <div class="legal">
    <span>Copyright © 2024 Varnoki.com – Powered by Crateloom</span>
    <span class="up"><svg width="10" height="6" viewBox="0 0 10 6"><path d="M1 5l4-4 4 4" fill="none" stroke="#aaa"/></svg></span>
  </div>
</footer>

</body>
</html>
```